Construction company focused on concrete and shed construction.

We need to update our current business card for brindlebuilds.com.au we would like an eye catching design with blue, grey and white incorporating our current logo.
Our company started off in concreting and due to varying factors we have expanded to include shed construction as well.
This has led to our current Logo looking a little out of place and somehow need to use the card to bring in the shed construction side of the business while not having to change current concrete look "BRINDLE" logo as we already have this incorporated into our company clothing and are not willing to change this yet.
Photo image attached for inspiration/ visual reference of type of work, not to be used on final design.
Please no cheesy designs of men in hard hats and tools
Final design should demonstrate a modern and service focused company.

Target Market(s)

Farmers, Business owners, Developers, Architects, Commercial project delivery

Industry/Entity Type

Construction Company

Contact Information for Business Card

Brindle Builds.
7c Harcourt st
South Launceston Tas
03 62918730

Font styles to use
Other font styles liked:
• see font in logo

Colors
3176b5
b2b2b2

Requirements
Must have
• Easy to read font,
• good contrast between back ground and writing
Nice to have
• Modern and corporate look with a fun but professional image.
Should not have
• Comic images or shadow images of tools/ people.

```html
<!DOCTYPE html>
<html lang="en">
<head>
<meta charset="utf-8">
<title>Brindle Builds – Business Card</title>
<link rel="stylesheet" href="https://fonts.googleapis.com/css2?family=Exo+2:wght@600;700&family=Roboto:wght@400;500&display=swap">
<style>
  :root {
    --page-bg: #d9d6d2;
    --card-bg: #eef0f1;
    --card-edge: #c9cdd0;
    --brand-blue: #3176b5;
    --name-blue: #1f5f96;
    --brand-grey: #b2b2b2;
    --tag-grey: #666a6e;
    --text-dark: #2b2d30;
  }
  html, body {
    margin: 0;
    width: 1200px;
    height: 1054px;
    overflow: hidden;
    background: var(--page-bg);
  }
  .card {
    position: absolute;
    left: 172px;
    top: 293px;
    width: 856px;
    height: 517px;
    background: var(--card-bg);
    border: 1px solid var(--card-edge);
    box-sizing: border-box;
    font-family: "Roboto", sans-serif;
    color: var(--text-dark);
  }
  .brand-block {
    position: absolute;
    left: 529px;
    top: 100px;
    width: 290px;
    display: flex;
    flex-direction: column;
    align-items: center;
    gap: 12px;
  }
  .brand-mark {
    display: flex;
    align-items: center;
    gap: 12px;
  }
  .brand-dot {
    width: 36px;
    height: 36px;
    border-radius: 50%;
    background: var(--brand-blue);
  }
  .brand-word {
    font-family: "Exo 2", sans-serif;
    font-weight: 700;
    font-size: 42px;
    line-height: 1;
    color: var(--brand-blue);
    letter-spacing: 1px;
  }
  .brand-services {
    margin: 0;
    padding-top: 10px;
    border-top: 2px solid var(--brand-grey);
    font-size: 15px;
    font-weight: 500;
    letter-spacing: 2px;
    text-transform: uppercase;
    color: var(--tag-grey);
    line-height: 1;
  }
  .person-name {
    position: absolute;
    left: 46px;
    top: 283px;
    margin: 0;
    font-family: "Exo 2", sans-serif;
    font-weight: 600;
    font-size: 32px;
    color: var(--name-blue);
    line-height: 1;
  }
  .person-role {
    position: absolute;
    left: 46px;
    top: 326px;
    margin: 0;
    font-size: 18px;
    line-height: 1;
  }
  .company-name {
    position: absolute;
    right: 38px;
    top: 330px;
    margin: 0;
    font-family: "Exo 2", sans-serif;
    font-weight: 700;
    font-size: 26px;
    color: var(--text-dark);
    letter-spacing: 0.5px;
    line-height: 1;
  }
  .divider {
    position: absolute;
    left: 38px;
    right: 38px;
    top: 371px;
    height: 2px;
    background: var(--name-blue);
  }
  .contact-list {
    position: absolute;
    left: 40px;
    top: 397px;
    margin: 0;
    padding: 0;
    list-style: none;
    font-size: 20px;
    line-height: 30px;
  }
  .contact-list li {
    display: flex;
    align-items: center;
    gap: 15px;
  }
  .contact-icon {
    width: 18px;
    height: 18px;
    fill: var(--name-blue);
    flex: none;
  }
  .address {
    position: absolute;
    right: 38px;
    top: 411px;
    margin: 0;
    font-style: normal;
    font-size: 20px;
    line-height: 31px;
    text-align: right;
  }
</style>
</head>
<body>
  <section class="card">
    <div class="brand-block">
      <div class="brand-mark">
        <span class="brand-dot"></span>
        <span class="brand-word">BRINDLE</span>
      </div>
      <p class="brand-services">Concreting &amp; Sheds</p>
    </div>

    <h1 class="person-name">Employee Name</h1>
    <p class="person-role">Managing Director</p>
    <h2 class="company-name">BRINDLE BUILDS</h2>
    <div class="divider"></div>

    <ul class="contact-list">
      <li>
        <svg class="contact-icon" viewBox="0 0 24 24" aria-hidden="true">
          <path d="M3 8c0-3 4-5 9-5s9 2 9 5v2h-5V8c-1-1-7-1-8 0v2H3z"/>
          <path d="M6 12h12l2 8H4z"/>
        </svg>
        <span>03 62918730</span>
      </li>
      <li>
        <svg class="contact-icon" viewBox="0 0 24 24" aria-hidden="true">
          <path d="M2 5h20v14H2z M4 7v1l8 5 8-5V7l-8 5z" fill-rule="evenodd"/>
        </svg>
        <span>name@brindlebuilds.com</span>
      </li>
      <li>
        <svg class="contact-icon" viewBox="0 0 24 24" aria-hidden="true">
          <path d="M12 2a10 10 0 1 0 0 20 10 10 0 0 0 0-20zm0 2c1.5 1.5 2.5 4 2.7 7H9.3C9.5 8 10.5 5.5 12 4zM4.1 11a8 8 0 0 1 3.6-5.8C7 7 7.4 9 7.3 11zm0 2h3.2c.1 2 .5 4 1.3 5.8A8 8 0 0 1 4.1 13zm5.2 0h5.4c-.2 3-1.2 5.5-2.7 7-1.5-1.5-2.5-4-2.7-7zm7.4 0h3.2a8 8 0 0 1-3.6 5.8c.7-1.8 1.1-3.8 1.1-5.8zm0-2c0-2-.4-4-1.2-5.8a8 8 0 0 1 4.4 5.8z"/>
        </svg>
        <span>www.brindlebuilds.com</span>
      </li>
    </ul>

    <address class="address">
      7C Harcourt St South<br>
      Launceston TAS
    </address>
  </section>
</body>
</html>
```